Business Card Design Project

This design is a slimline business card 45mm x90mm, the card will be printed at 49mm x 94mm and cut to 45mm x90 mm, this needs to be considered in the design. The content required on the front and back of the business card is attached in a pdf; the design will be done using photo shop as we use CS6 in our business. The design needs to be developed using a CMYK colour pallet, the main colours used on our business are red, grey black and white. A snapshot of our business brochure and new website has been provided to give you an understanding on our businesses look and feel.
FRONT OF BUSINESS CARD
Director
Marcus Feld
Ph+61 0421780213
www.brightvanecontracting.com.au
marcusfeld@brightvanecontracting.com.au
BACK OF BUSINESS CARD
SUPPORTING CLIENTS IN
Oil & Gas I Minerals & Metals I Petrochemical I Manufacturing
Building & Construction I Telecommunication I Rail I Civil I New Industries
KNOWLEDGE I EXPERTISE I EXPERIENCE I CAPACITY

```html
<!DOCTYPE html>
<html lang="en">
<head>
<meta charset="utf-8">
<title>Brightvane Contracting – Business Card</title>
<link href="https://fonts.googleapis.com/css2?family=Raleway:wght@400;500;700;800&display=swap" rel="stylesheet">
<style>
  :root {
    --canvas: #e8e8e8;
    --card-white: #ffffff;
    --brand-red: #ec1c24;
    --ink: #1e1e1e;
    --grey: #5a5a5a;
  }
  * { margin: 0; padding: 0; box-sizing: border-box; }
  html, body {
    width: 1200px; height: 1000px; overflow: hidden;
    background: var(--canvas);
    font-family: "Raleway", Arial, sans-serif;
  }
  .canvas { position: relative; width: 1200px; height: 1000px; }

  .card { position: absolute; width: 555px; height: 290px; overflow: hidden; }

  /* Front */
  .card-front { left: 29px; top: 41px; background: var(--card-white); }
  .brand { position: absolute; left: 30px; top: 50px; display: flex; align-items: center; gap: 12px; }
  .brand-dot { width: 22px; height: 22px; border-radius: 50%; background: var(--brand-red); }
  .brand-name { font-weight: 800; font-size: 28px; color: var(--ink); letter-spacing: -0.3px; line-height: 1; }
  .brand-tagline {
    position: absolute; left: 64px; top: 87px;
    font-size: 9px; font-weight: 500; color: var(--ink);
  }
  .role { position: absolute; left: 30px; top: 147px; font-size: 15px; color: var(--grey); }
  .person { position: absolute; left: 30px; top: 167px; font-size: 20px; font-weight: 700; color: var(--ink); }
  .contacts { position: absolute; left: 30px; top: 211px; list-style: none; font-size: 13px; color: var(--ink); line-height: 18px; }
  .contacts .label { display: inline-block; width: 24px; color: var(--brand-red); }

  /* Back */
  .card-back { left: 609px; top: 254px; background: var(--brand-red); color: #fff; }
  .sectors-title { position: absolute; left: 36px; top: 37px; font-size: 14px; font-weight: 800; letter-spacing: 0.2px; }
  .sectors { position: absolute; left: 36px; top: 76px; list-style: none; font-size: 16px; font-weight: 500; line-height: 20px; letter-spacing: 0.3px; }
  .values {
    position: absolute; left: 36px; top: 243px; display: flex; align-items: center;
    font-size: 17px; font-weight: 800; letter-spacing: 0.5px;
  }
  .values .sep { width: 1px; height: 13px; background: rgba(255,255,255,0.7); margin: 0 14px; }
</style>
</head>
<body>
<main class="canvas">
  <section class="card card-front" aria-label="Business card front">
    <div class="brand">
      <span class="brand-dot"></span>
      <span class="brand-name">BRIGHTVANE CONTRACTING</span>
    </div>
    <p class="brand-tagline">Delivering Reliable Site Planning and Contract Delivery Services</p>
    <p class="role">Director</p>
    <p class="person">Marcus Feld</p>
    <ul class="contacts">
      <li><span class="label">p.</span>+61 0497365128</li>
      <li><span class="label">w.</span>brightvanecontracting.com.au</li>
      <li><span class="label">e.</span>marcusfeld@brightvanecontracting.com.au</li>
    </ul>
  </section>

  <section class="card card-back" aria-label="Business card back">
    <h2 class="sectors-title">SUPPORTING CLIENTS IN</h2>
    <ul class="sectors">
      <li>Oil &amp; Gas I Minerals &amp; Metals I Petrochemical</li>
      <li>Manufacturing | Building &amp; Construction</li>
      <li>Telecommunication I Rail I Civil</li>
      <li>New Industries</li>
    </ul>
    <div class="values">
      <span>KNOWLEDGE</span><span class="sep"></span>
      <span>EXPERTISE</span><span class="sep"></span>
      <span>EXPERIENCE</span><span class="sep"></span>
      <span>CAPACITY</span>
    </div>
  </section>
</main>
</body>
</html>
```